Promotional business a5 Notepad design

I am looking for a custom a5 notepad design as a promotional item to give away to customers etc.
Attached will be a desk planner we had designed feel free to use as a reference.
We want the notepad to have lines running horizontal not squares like the desk planner example.

Industry/Entity Type

Hydraulic / industrial

Colors

Designer to choose colors to be used in the design.

```html
<!DOCTYPE html>
<html lang="en">
<head>
<meta charset="utf-8">
<title>Meridian Hose and Couplings – A5 Notepad</title>
<link rel="stylesheet" href="https://fonts.googleapis.com/css2?family=Work+Sans:wght@400;500;600;700&display=swap">
<style>
  :root {
    --brand-blue: #2b4a9e;
    --brand-yellow: #fdc41a;
    --ink-black: #111111;
    --logo-grey: #2a2a2a;
    --rule-grey: #9a9a9a;
    --paper: #ffffff;
  }
  * { margin: 0; padding: 0; box-sizing: border-box; }
  html, body { width: 849px; height: 1200px; overflow: hidden; background: var(--paper); }
  .notepad {
    position: relative;
    width: 849px;
    height: 1200px;
    background: var(--paper);
    font-family: "Work Sans", Arial, sans-serif;
  }
  .header-art { position: absolute; top: 0; left: 0; width: 849px; height: 140px; }
  .brand {
    position: absolute;
    left: 40px;
    top: 62px;
    display: flex;
    align-items: center;
    gap: 12px;
  }
  .brand-mark {
    width: 64px;
    height: 64px;
    border-radius: 50%;
    background: var(--logo-grey);
  }
  .brand-name {
    color: var(--brand-blue);
    font-weight: 700;
    font-size: 25px;
    line-height: 1.05;
    letter-spacing: 0.5px;
    text-transform: uppercase;
  }
  .contact {
    position: absolute;
    right: 44px;
    top: 30px;
    list-style: none;
    color: var(--paper);
    font-size: 14.5px;
    font-weight: 500;
    letter-spacing: 0.6px;
    text-align: right;
  }
  .contact li { display: flex; justify-content: flex-end; align-items: flex-start; gap: 8px; }
  .contact li + li { margin-top: 6px; }
  .contact .area { line-height: 17px; margin-bottom: 6px; }
  .contact .icon { width: 20px; height: 17px; flex: none; fill: var(--brand-yellow); }
  .writing-lines { position: absolute; left: 42px; top: 229px; width: 757px; list-style: none; }
  .writing-lines li { height: 36.29px; border-top: 1px solid var(--rule-grey); }
  .footer-band {
    position: absolute;
    left: 0; bottom: 0;
    width: 849px; height: 58px;
    background: var(--brand-blue);
    color: var(--paper);
    display: flex; align-items: center; justify-content: center;
    font-weight: 700;
    font-size: 18px;
    letter-spacing: 0.3px;
    padding-top: 2px;
  }
</style>
</head>
<body>
<main class="notepad">
  <svg class="header-art" viewBox="0 0 849 140" aria-hidden="true">
    <polygon points="0,0 388,0 408,34 0,34" fill="var(--brand-yellow)"/>
    <path d="M378,0 L849,0 L849,138 L522,138 C478,138 458,118 438,86 Z" fill="var(--ink-black)"/>
    <path d="M392,0 L849,0 L849,138 L528,138 C490,136 470,116 452,84 Z" fill="var(--brand-blue)"/>
  </svg>

  <div class="brand">
    <span class="brand-mark"></span>
    <span class="brand-name">Meridian<br>Hose &amp; Couplings</span>
  </div>

  <ul class="contact">
    <li class="area"><span>SERVICING THE ADELAIDE<br>METROPOLITAN AREA</span>
      <svg class="icon" viewBox="0 0 20 17"><path d="M10 0a6 6 0 0 0-6 6c0 4.5 6 11 6 11s6-6.5 6-11a6 6 0 0 0-6-6zm0 8.5a2.5 2.5 0 1 1 0-5 2.5 2.5 0 0 1 0 5z"/></svg></li>
    <li><span>EMAIL@MERIDIANHOSE.COM.AU</span>
      <svg class="icon" viewBox="0 0 20 17"><path d="M2 3h16v1.5l-8 5-8-5zM2 6.3l8 5 8-5V14H2z"/></svg></li>
    <li><span>GENERAL ENQUIRIES: 08 8123 4567</span>
      <svg class="icon" viewBox="0 0 20 17"><path d="M1 6c0-2 3-4 9-4s9 2 9 4v1.5h-4.5V5.5h-9v2H1zM4 9l3-3h6l3 3v6H4zm6 1a2 2 0 1 0 0 4 2 2 0 0 0 0-4z"/></svg></li>
  </ul>

  <ol class="writing-lines" aria-hidden="true">
    <li></li><li></li><li></li><li></li><li></li>
    <li></li><li></li><li></li><li></li><li></li>
    <li></li><li></li><li></li><li></li><li></li>
    <li></li><li></li><li></li><li></li><li></li>
    <li></li><li></li><li></li><li></li><li></li>
  </ol>

  <footer class="footer-band">INDUSTRY CHOSEN HOSE AND FITTINGS PROVIDER</footer>
</main>
</body>
</html>
```